Global recruitment firm needs a design for marketing material

We need a design for our company Harrow Prime, which is a global recruitment firm specializing in senior finance and executive positions. This will be a template/ background for all our marketing material. We are looking to communicate a consistent message to current and existing clients. Uploaded below are our files describing our mission, values and strategy and story. Please also look at our website www.harrowprime.com.au. Examples of where this design will be used will be in client proposals, marketing info telling our story, social media content, infographics, and general client communication.

Target Market(s)

Client companies in the finance industry, Executive level finance candidates(CEO, CFO)

Requirements
Must have
• company logo, mission, value, strategy, website, our story
• Will be using the graphic for website, all communication with clients > looking for something to use for different purposes

```html
<!DOCTYPE html>
<html lang="en">
<head>
<meta charset="utf-8">
<title>Harrow Prime</title>
<link href="https://fonts.googleapis.com/css2?family=Montserrat:wght@400;500;600;800;900&family=EB+Garamond:wght@500&display=swap" rel="stylesheet">
<style>
  :root {
    --navy: #0e1430;
    --navy-mid: #1d2550;
    --blue: #0b6cc0;
    --blue-dark: #0856a3;
    --blue-bright: #1e8fe0;
    --blue-light: #6cc6f2;
    --heading-blue: #1266b4;
    --text: #333a44;
    --white: #ffffff;
    --shadow-grey: #c9ccd1;
  }
  * { margin: 0; padding: 0; box-sizing: border-box; }
  html, body { width: 733px; height: 1200px; overflow: hidden; background: var(--white); }
  .canvas {
    position: relative; width: 733px; height: 1200px; overflow: hidden;
    font-family: "Montserrat", Arial, sans-serif; color: var(--text); background: var(--white);
  }
  .layer { position: absolute; left: 0; top: 0; }
  .hero-photo {
    position: absolute; left: 0; top: 0; width: 733px; height: 440px;
    background:
      radial-gradient(ellipse 60% 30% at 55% 58%, rgba(190,150,80,.45), transparent 70%),
      linear-gradient(180deg, #0b1030 0%, #1a2150 45%, #2b2a35 62%, #0d1326 100%);
  }
  .brand {
    position: absolute; left: 26px; top: 30px;
    font-family: "Montserrat", Arial, sans-serif; font-weight: 600; font-size: 15px;
    color: var(--blue-bright); letter-spacing: .5px; display: flex; align-items: center; gap: 6px;
  }
  .brand-square { width: 9px; height: 9px; background: var(--blue-bright); }
  .hero-title {
    position: absolute; left: 0; width: 733px; top: 134px; text-align: center;
    font-family: "EB Garamond", Georgia, serif; font-weight: 500; font-size: 25px;
    color: var(--white); letter-spacing: .5px;
  }
  .pillar { position: absolute; top: 458px; }
  .pillar h2, .strategy h2 {
    font-weight: 900; font-size: 18px; color: var(--heading-blue); letter-spacing: .3px;
  }
  .pillar p { font-size: 5.6px; line-height: 11px; margin-top: 12px; width: 120px; }
  .pillar-mission { left: 152px; }
  .pillar-values { left: 299px; }
  .pillar-vision { left: 465px; }
  .pillar-vision p { width: 125px; }
  .values-list { list-style: none; margin-top: 12px; }
  .values-list li { display: flex; align-items: center; gap: 7px; font-size: 5.6px; height: 21px; }
  .values-list svg { width: 10px; height: 8px; flex: none; }
  .tagline { position: absolute; left: 0; width: 733px; text-align: center; color: var(--white); }
  .tagline-main { top: 646px; font-weight: 800; font-size: 17px; letter-spacing: .3px; }
  .tagline-sub { top: 672px; font-weight: 500; font-size: 17px; letter-spacing: 2.6px; }
  .strategy { position: absolute; left: 153px; top: 779px; width: 200px; }
  .strategy h3 { font-weight: 500; font-size: 13.5px; color: var(--heading-blue); margin-top: 6px; }
  .strategy p { font-size: 6.4px; margin-top: 3px; }
  .strategy h3.first { margin-top: 5px; }
  .advantage-list { list-style: none; margin-top: 8px; }
  .advantage-list li { display: flex; gap: 10px; font-size: 6.4px; line-height: 11px; margin-bottom: 6px; width: 200px; }
  .advantage-list svg { width: 9px; height: 8px; flex: none; margin-top: 2px; }
  .team-photo { position: absolute; left: 360px; top: 760px; }
</style>
</head>
<body>
<div class="canvas">
  <div class="hero-photo" role="img" aria-label="Night view of an illuminated arch bridge over a river with city lights reflected in the water"></div>

  <svg class="layer" width="733" height="1200" viewBox="0 0 733 1200" aria-hidden="true">
    <defs>
      <linearGradient id="sweepLight" x1="0" y1="0" x2="1" y2="0">
        <stop offset="0" stop-color="#7fd0f5"/>
        <stop offset=".5" stop-color="#3aaae8"/>
        <stop offset="1" stop-color="#1670c4"/>
      </linearGradient>
      <linearGradient id="sweepDeep" x1="0" y1="0" x2="1" y2="1">
        <stop offset="0" stop-color="#1c8ee0"/>
        <stop offset="1" stop-color="#0b5fb0"/>
      </linearGradient>
      <linearGradient id="cityFill" x1="0" y1="0" x2="1" y2="0">
        <stop offset="0" stop-color="#12528f"/>
        <stop offset=".5" stop-color="#1466b5"/>
        <stop offset="1" stop-color="#0d5aa6"/>
      </linearGradient>
    </defs>
    <!-- hero sweeps -->
    <path d="M0,176 C140,270 330,322 500,330 C610,335 690,300 733,245 L733,440 C620,372 470,350 300,362 C170,370 70,372 0,370 Z" fill="url(#sweepDeep)"/>
    <path d="M0,240 C110,330 280,350 470,340 C600,334 680,372 733,436 C620,400 430,405 240,412 C120,416 40,406 0,392 Z" fill="url(#sweepLight)"/>
    <path d="M20,392 C180,428 360,422 500,404 C610,392 690,408 733,438 C650,418 540,418 420,428 C280,440 120,434 20,392 Z" fill="var(--shadow-grey)"/>
    <path d="M0,382 C160,418 330,418 480,400 C600,386 680,404 733,436 L733,560 L0,560 Z" fill="var(--white)"/>
    <!-- tagline band -->
    <path d="M0,606 C200,590 460,578 733,598 L733,722 C520,710 260,718 0,742 Z" fill="var(--blue)"/>
    <!-- closing band -->
    <path d="M0,1040 C150,1024 300,1028 450,1046 C590,1062 680,1052 733,1040 L733,1200 L0,1200 Z" fill="url(#cityFill)" role="img" aria-label="Blue-toned city skyline with a businessman silhouette"/>
  </svg>

  <div class="brand"><span class="brand-square"></span>Harrow Prime</div>
  <h1 class="hero-title">HARROW PRIME</h1>

  <section class="pillar pillar-mission">
    <h2>MISSION</h2>
    <p>To help financial professionals to connect to opportunities globally</p>
  </section>

  <section class="pillar pillar-values">
    <h2>VALUES</h2>
    <ul class="values-list">
      <li><svg viewBox="0 0 10 8"><path d="M1 1l3 3-3 3M5 1l3 3-3 3" fill="none" stroke="#1266b4" stroke-width="1.2"/></svg>Transparency</li>
      <li><svg viewBox="0 0 10 8"><path d="M1 1l3 3-3 3M5 1l3 3-3 3" fill="none" stroke="#1266b4" stroke-width="1.2"/></svg>Help &amp; Support hiring decision - Hiring partner</li>
      <li><svg viewBox="0 0 10 8"><path d="M1 1l3 3-3 3M5 1l3 3-3 3" fill="none" stroke="#1266b4" stroke-width="1.2"/></svg>To make better hiring decisions</li>
      <li><svg viewBox="0 0 10 8"><path d="M1 1l3 3-3 3M5 1l3 3-3 3" fill="none" stroke="#1266b4" stroke-width="1.2"/></svg>Relationship with Clients and Candidates</li>
    </ul>
  </section>

  <section class="pillar pillar-vision">
    <h2>VISION</h2>
    <p>To be the number 1 partner to our Clients in solving their business problems with people solutions</p>
  </section>

  <div class="tagline tagline-main">CONNECTING TALENT</div>
  <div class="tagline tagline-sub">with Opportunity Globally</div>

  <section class="strategy">
    <h2>STRATEGY</h2>
    <h3 class="first">OBJECTIVE</h3>
    <p>To be our Clients number 1 recruitment partner by 2020</p>
    <h3>SCOPE</h3>
    <p>Finance professionals globally</p>
    <h3>COMPETITIVE ADVANTAGE</h3>
    <ul class="advantage-list">
      <li><svg viewBox="0 0 9 8"><path d="M0 4h7M4 1l3 3-3 3" fill="none" stroke="#1266b4" stroke-width="1.4"/></svg>Tacit knowledge of Client business</li>
      <li><svg viewBox="0 0 9 8"><path d="M0 4h7M4 1l3 3-3 3" fill="none" stroke="#1266b4" stroke-width="1.4"/></svg>Relationships Big investment- Know our people beyond recruitment process-many touch points-</li>
      <li><svg viewBox="0 0 9 8"><path d="M0 4h7M4 1l3 3-3 3" fill="none" stroke="#1266b4" stroke-width="1.4"/></svg>Our process ensures hiring decisions-Has-Coaching people- No surprises</li>
      <li><svg viewBox="0 0 9 8"><path d="M0 4h7M4 1l3 3-3 3" fill="none" stroke="#1266b4" stroke-width="1.4"/></svg>Only 2 backouts- Inform candidate onpitfalls/culture problems/upside</li>
    </ul>
  </section>

  <svg class="team-photo" width="260" height="260" viewBox="0 0 260 260" role="img" aria-label="Team of colleagues giving high fives around an office table">
    <defs>
      <radialGradient id="officeTone" cx=".5" cy=".4" r=".6">
        <stop offset="0" stop-color="#f2f5f8"/>
        <stop offset=".6" stop-color="#c9d3dd"/>
        <stop offset="1" stop-color="#5b6b80"/>
      </radialGradient>
    </defs>
    <circle cx="130" cy="130" r="127" fill="url(#officeTone)" stroke="#1266b4" stroke-width="3"/>
  </svg>
</div>
</body>
</html>
```